Business Card- Can you make it cool vs boring!

Need a refresh on my business card! Want it to be modern but simple, classic and a pop of coolness! we do senior living and it is boring. but that doesn't mean our business card have to look boring! Open to two sided cards. our website is www.Bruvel-HQ.com

Target Market(s)

capital market

Industry/Entity Type

senior housing/ real estate

Contact Information for Business Card

logo/ name/ cell/ address/ www.Bruvel-HQ.com/ space for a QR code

Requirements
Must have
• maybe a QR code (do not make prominent I may not use the QR so design where it can be taken out) that link to more about us/ landing page. needs to be modern but clean
Should not have
• clip art or script

```html
<!DOCTYPE html>
<html lang="en">
<head>
<meta charset="utf-8">
<title>Bruvel Living – Business Card</title>
<link rel="stylesheet" href="https://fonts.googleapis.com/css2?family=Poppins:wght@300;400;500&display=swap">
<style>
  :root {
    --backdrop: #2b2b2c;
    --card: #1d1e20;
    --accent: #c0561f;
    --text-soft: #a3a3a3;
    --text-light: #c4c4c4;
    --rule: #6a6a6a;
  }
  * { box-sizing: border-box; margin: 0; padding: 0; }
  html, body { width: 1200px; height: 1108px; overflow: hidden; }
  body {
    background: var(--backdrop);
    font-family: "Poppins", sans-serif;
    position: relative;
  }
  .card {
    position: absolute;
    top: 244px;
    width: 400px;
    height: 620px;
    background: var(--card);
    border-radius: 22px;
    box-shadow: 0 18px 40px rgba(0,0,0,0.45);
    overflow: hidden;
  }
  .card--front { left: 150px; }
  .card--back { left: 650px; }

  .brand {
    position: absolute;
    top: 150px;
    left: 0; right: 0;
    text-align: center;
    font-size: 44px;
    font-weight: 500;
    color: var(--accent);
    letter-spacing: 1px;
  }
  .holder {
    position: absolute;
    top: 330px;
    left: 0; right: 0;
    text-align: center;
  }
  .holder__name {
    font-size: 30px;
    font-weight: 400;
    color: var(--accent);
    line-height: 1.1;
  }
  .holder__title {
    margin-top: 6px;
    font-size: 15px;
    font-weight: 400;
    letter-spacing: 1px;
    color: var(--text-soft);
  }
  .icon-row {
    position: absolute;
    top: 410px;
    left: 40px; right: 40px;
    display: flex;
    align-items: center;
    gap: 8px;
  }
  .icon-row__rule { flex: 1; height: 1px; background: var(--rule); }
  .icon-row__icon {
    width: 30px; height: 30px;
    background: var(--accent);
    border-radius: 4px;
    display: flex; align-items: center; justify-content: center;
  }
  .contact {
    position: absolute;
    top: 452px;
    left: 0; right: 0;
    text-align: center;
    font-size: 16px;
    line-height: 25px;
    color: var(--text-light);
  }
  .contact__accent { color: var(--accent); }
  .divider {
    position: absolute;
    top: 538px;
    left: 60px; right: 60px;
    height: 1px;
    background: var(--rule);
  }
  .address {
    position: absolute;
    top: 550px;
    left: 0; right: 0;
    text-align: center;
    font-size: 15px;
    line-height: 23px;
    color: var(--text-soft);
  }

  .back-pattern {
    position: absolute;
    inset: 0;
    background: linear-gradient(135deg, #2a2b2e 0%, #1d1e20 55%, #18191a 100%);
  }
  .back-brand {
    position: absolute;
    top: 470px;
    left: 0; right: 0;
    text-align: center;
    font-size: 24px;
    font-weight: 500;
    color: var(--accent);
  }
</style>
</head>
<body>
  <section class="card card--front">
    <div class="brand">Bruvel Living</div>
    <div class="holder">
      <div class="holder__name">Marcus Hale</div>
      <div class="holder__title">MANAGING DIRECTOR</div>
    </div>
    <div class="icon-row">
      <span class="icon-row__rule"></span>
      <span class="icon-row__icon">
        <svg width="18" height="18" viewBox="0 0 24 24" aria-label="Phone"><path fill="#1d1e20" d="M6.6 10.8a15 15 0 0 0 6.6 6.6l2.2-2.2c.3-.3.7-.4 1-.2 1.1.4 2.3.6 3.6.6.6 0 1 .4 1 1V20c0 .6-.4 1-1 1A17 17 0 0 1 3 4c0-.6.4-1 1-1h3.5c.6 0 1 .4 1 1 0 1.3.2 2.5.6 3.6.1.3 0 .7-.2 1z"/></svg>
      </span>
      <span class="icon-row__icon">
        <svg width="18" height="18" viewBox="0 0 24 24" aria-label="Email"><rect x="3" y="5" width="18" height="14" rx="1.5" fill="none" stroke="#1d1e20" stroke-width="2"/><path d="M3 6l9 7 9-7" fill="none" stroke="#1d1e20" stroke-width="2"/></svg>
      </span>
      <span class="icon-row__icon">
        <svg width="18" height="18" viewBox="0 0 24 24" aria-label="Website"><circle cx="12" cy="12" r="9" fill="none" stroke="#1d1e20" stroke-width="2"/><path d="M3 12h18M12 3c3 3.5 3 14.5 0 18M12 3c-3 3.5-3 14.5 0 18" fill="none" stroke="#1d1e20" stroke-width="1.6"/></svg>
      </span>
      <span class="icon-row__rule"></span>
    </div>
    <div class="contact">
      <div>044-555 210 480</div>
      <div>hello@bruvelmail.com</div>
      <div>www.<span class="contact__accent">Bruvel-HQ</span>.com</div>
    </div>
    <div class="divider"></div>
    <div class="address">
      <div>421, Address line goes here</div>
      <div>45452, Country Name</div>
    </div>
  </section>

  <section class="card card--back">
    <div class="back-pattern" role="img" aria-label="Faint repeating brand-name pattern on a dark background"></div>
    <div class="back-brand">Bruvel Living</div>
  </section>
</body>
</html>
```